Talmora Inc., a third party debt collection agency needs a Website

Talmora needs a very basic website (3 basic pages) so that consumers can download forms, potential employees can get required EEO language and see potential jobs, and to show that they are a consumer friendly organization.

I've attached a list of requirements and wishes titled "Talmora Website Specifications"

Target Market(s)

Consumers that need to repay their government loans; Talmora will walk through the process to assist them.

Industry/Entity Type

Financial Service

Coding

Coded - Design and coding required

Number of Pages Required

1 page

Font styles to use
Sans Serif

Colors
0355a3

Requirements
Must have
• Talmora Logo
• See document "Talmora Website Specifications" for all requirements

```html
<!DOCTYPE html>
<html lang="en">
<head>
<meta charset="utf-8">
<title>Talmora, Inc.</title>
<link rel="stylesheet" href="https://fonts.googleapis.com/css2?family=Open+Sans:wght@400;600;700&display=swap">
<style>
  :root {
    --brand-red: #8e1b20;
    --brand-red-soft: rgba(128, 28, 34, 0.84);
    --ink: #333333;
    --muted: #7a7a7a;
    --rule: #dddddd;
    --button: #eeeeee;
    --footer: #3a3a3a;
    --footer-text: #b5b5b5;
    --badge-dark: #4b4b4b;
    --badge-light: #f4f4f4;
    --white: #ffffff;
  }
  * { box-sizing: border-box; margin: 0; padding: 0; }
  html, body { width: 1120px; height: 1200px; overflow: hidden; }
  body {
    font-family: "Open Sans", Arial, sans-serif;
    background: var(--white);
    color: var(--ink);
    position: relative;
  }

  .site-header { position: absolute; left: 0; top: 0; width: 1120px; height: 104px; }
  .brand {
    position: absolute; left: 123px; top: 46px;
    display: flex; align-items: center; gap: 9px;
    font-size: 27px; font-weight: 700; color: var(--brand-red); line-height: 1;
  }
  .brand-dot { width: 15px; height: 15px; border-radius: 50%; background: var(--brand-red); }
  .main-nav {
    position: absolute; left: 496px; top: 44px;
    display: flex; gap: 27px; font-size: 10.7px; line-height: 1;
  }
  .main-nav a { color: var(--ink); text-decoration: none; }
  .main-nav a.is-current { color: var(--brand-red); }

  .hero {
    position: absolute; left: 0; top: 104px; width: 1120px; height: 468px;
    background:
      radial-gradient(ellipse 170px 230px at 820px 250px, rgba(226, 190, 170, 0.95), rgba(226, 190, 170, 0) 100%),
      radial-gradient(ellipse 260px 330px at 830px 230px, rgba(92, 58, 44, 0.85), rgba(92, 58, 44, 0) 100%),
      radial-gradient(ellipse 260px 120px at 830px 470px, rgba(245, 242, 240, 0.95), rgba(245, 242, 240, 0) 100%),
      radial-gradient(ellipse 200px 160px at 380px 430px, rgba(70, 78, 96, 0.55), rgba(70, 78, 96, 0) 100%),
      radial-gradient(ellipse 120px 170px at 30px 390px, rgba(150, 110, 95, 0.55), rgba(150, 110, 95, 0) 100%),
      linear-gradient(180deg, #e4e8ea 0%, #d5dadd 55%, #c9ced2 100%);
  }
  .hero-caption {
    position: absolute; left: 123px; top: 143px; width: 422px; height: 183px;
    background: var(--brand-red-soft); color: var(--white);
    padding: 11px 15px 0 17px;
  }
  .hero-caption h1 { font-size: 28.5px; font-weight: 700; line-height: 1.2; margin-bottom: 7px; letter-spacing: -0.2px; }
  .hero-caption p { font-size: 10.6px; line-height: 19.4px; letter-spacing: -0.1px; }
  .slider-dots {
    position: absolute; left: 523px; top: 425px; width: 73px; height: 17px;
    border-radius: 9px; background: rgba(40, 40, 50, 0.6);
    display: flex; align-items: center; justify-content: center; gap: 8px;
  }
  .slider-dots span { width: 7px; height: 7px; border-radius: 50%; background: var(--white); }
  .slider-dots span.is-active { background: transparent; border: 1.5px solid var(--white); }

  .features {
    position: absolute; left: 123px; top: 612px; width: 874px;
    display: flex; gap: 35px;
  }
  .feature { width: 268px; }
  .feature-image { height: 165px; border-bottom: 5px solid var(--brand-red); }
  .feature-image.team {
    background:
      radial-gradient(ellipse 70px 90px at 190px 80px, rgba(222, 186, 165, 0.9), rgba(222, 186, 165, 0) 100%),
      radial-gradient(ellipse 60px 80px at 75px 95px, rgba(190, 150, 130, 0.7), rgba(190, 150, 130, 0) 100%),
      linear-gradient(180deg, #b9cde0 0%, #dfe6ee 55%, #c9d2dc 100%);
  }
  .feature-image.payment {
    background:
      radial-gradient(ellipse 70px 30px at 134px 90px, rgba(214, 206, 180, 0.85), rgba(214, 206, 180, 0) 100%),
      radial-gradient(ellipse 170px 110px at 134px 60px, #8d8d8d, rgba(141, 141, 141, 0) 100%),
      linear-gradient(180deg, #585858 0%, #6e6e6e 50%, #4c4c4c 100%);
  }
  .feature-image.office {
    background:
      radial-gradient(ellipse 110px 50px at 140px 130px, rgba(250, 250, 250, 0.95), rgba(250, 250, 250, 0) 100%),
      radial-gradient(ellipse 90px 60px at 150px 55px, rgba(90, 90, 95, 0.6), rgba(90, 90, 95, 0) 100%),
      linear-gradient(180deg, #d8d6d2 0%, #ecebe8 60%, #f4f4f3 100%);
  }
  .feature h2 {
    font-size: 18.5px; font-weight: 400; color: var(--brand-red); line-height: 1;
    margin-top: 15px; margin-bottom: 7px;
  }
  .feature p { font-size: 9.4px; line-height: 16.4px; color: var(--muted); }
  .read-more {
    display: inline-block; margin-top: 10px; width: 74px; text-align: center;
    height: 31px; line-height: 31px; font-size: 9.6px;
    background: var(--button); color: #555; text-decoration: none;
  }

  .section-rule { position: absolute; left: 123px; top: 944px; width: 874px; height: 1px; background: var(--rule); }
  .clients-title {
    position: absolute; left: 0; top: 976px; width: 1120px; text-align: center;
    font-size: 11.5px; font-weight: 400; color: var(--muted); line-height: 1;
  }
  .client-list {
    position: absolute; left: 123px; top: 1013px; width: 874px;
    display: flex; justify-content: space-between; align-items: center; list-style: none;
  }
  .client-list li { font-size: 11.5px; font-weight: 600; color: #444; white-space: nowrap; line-height: 16px; }

  .site-footer { position: absolute; left: 0; top: 1080px; width: 1120px; height: 120px; background: var(--footer); }
  .footer-nav { position: absolute; left: 124px; top: 24px; font-size: 9.6px; color: var(--footer-text); line-height: 1; }
  .footer-nav a { color: var(--footer-text); text-decoration: none; }
  .footer-nav .sep { margin: 0 8px; }
  .copyright { position: absolute; left: 124px; top: 49px; font-size: 9.6px; color: var(--footer-text); line-height: 1; }
  .social { position: absolute; left: 124px; top: 75px; display: flex; gap: 6px; }
  .social span { width: 25px; height: 25px; border-radius: 50%; border: 1.5px solid #5a5a5a; }
  .social .one { background: #3b5b9e; }
  .social .two { background: #2aa3e0; }
  .social .three { background: #1a7bb8; }
  .badge-accredited {
    position: absolute; left: 808px; top: 37px; width: 109px; height: 41px;
    border-radius: 4px; background: var(--badge-dark); border: 1px solid #5e5e5e;
  }
  .badge-accredited .badge-panel {
    position: absolute; left: 3px; top: 3px; width: 34px; height: 33px;
    border-radius: 3px; background: var(--badge-light);
  }
  .badge-member {
    position: absolute; left: 937px; top: 25px; width: 59px; height: 73px;
    background: linear-gradient(180deg, #8a8a8a 0%, #6a6a6a 45%, #474747 100%);
    border-radius: 2px;
  }
</style>
</head>
<body>
  <header class="site-header">
    <div class="brand"><span class="brand-dot"></span>Talmora, Inc.</div>
    <nav class="main-nav">
      <a class="is-current" href="#">Home</a>
      <a href="#">Our Process</a>
      <a href="#">Collection Rates</a>
      <a href="#">Clients</a>
      <a href="#">Careers</a>
      <a href="#">About Us</a>
      <a href="#">Contact Us</a>
    </nav>
  </header>

  <section class="hero" role="img" aria-label="Smiling customer service agent wearing a headset in a bright office with blurred colleagues behind">
    <div class="hero-caption">
      <h1>Welcome to Talmora</h1>
      <p>Talmora is a third party debt collection agency that is focused on the collection of higher education loans.&nbsp; Talmora is compliant with all federal, state, and local laws and is committed to the professional and fair treatment of consumers.&nbsp; Our goal is to assist consumers in resolving their obligations in the manner that best meets their needs and to provide information necessary in order for consumers to make an informed decision.</p>
    </div>
    <div class="slider-dots"><span class="is-active"></span><span></span><span></span><span></span></div>
  </section>

  <main class="features">
    <article class="feature">
      <div class="feature-image team" role="img" aria-label="Team of call center agents with headsets"></div>
      <h2>Our Process</h2>
      <p>Sed feugiat consequat dui in luctus. Aenean est orci laoreet vulputate vel et augue. In id ex ultrices purus egestas suscip-it eget tempus neque.</p>
      <a class="read-more" href="#">Read More</a>
    </article>
    <article class="feature">
      <div class="feature-image payment" role="img" aria-label="Hands passing a stack of banknotes"></div>
      <h2>Collection Rates</h2>
      <p>Sed feugiat consequat dui in luctus. Aenean est orci laoreet vulputate vel et augue. In id ex ultrices purus egestas suscip-it eget tempus neque.</p>
      <a class="read-more" href="#">Read More</a>
    </article>
    <article class="feature">
      <div class="feature-image office" role="img" aria-label="Row of office workstations with computers and headsets"></div>
      <h2>Careers</h2>
      <p>Sed feugiat consequat dui in luctus. Aenean est orci laoreet vulputate vel et augue. In id ex ultrices purus egestas suscip-it eget tempus neque.</p>
      <a class="read-more" href="#">Read More</a>
    </article>
  </main>

  <div class="section-rule"></div>
  <h3 class="clients-title">Clients</h3>
  <ul class="client-list">
    <li>Mira Hollis</li>
    <li>Lark Denim</li>
    <li>Cora Vale</li>
    <li>Westbrook Row</li>
    <li>Dana Merle</li>
    <li>Little Sprout</li>
    <li>Fernhill</li>
    <li>Harborline</li>
  </ul>

  <footer class="site-footer">
    <nav class="footer-nav">
      <a href="#">Home</a><span class="sep">|</span><a href="#">Our Process</a><span class="sep">|</span><a href="#">Collection Rates</a><span class="sep">|</span><a href="#">Clients</a><span class="sep">|</span><a href="#">Careers</a><span class="sep">|</span><a href="#">About Us</a><span class="sep">|</span><a href="#">Contact Us</a>
    </nav>
    <p class="copyright">Copyright &copy; 2016&nbsp; Talmora.&nbsp; All rights reserved.</p>
    <div class="social" aria-label="Social links"><span class="one"></span><span class="two"></span><span class="three"></span></div>
    <div class="badge-accredited" role="img" aria-label="Accreditation badge"><span class="badge-panel"></span></div>
    <div class="badge-member" role="img" aria-label="Trade association membership badge"></div>
  </footer>
</body>
</html>
```